professional business card

A Clean looking business card for a money transfer company. Our company is call Pavolex= Transfer + Send = Transcend (next level)
to show professionalism as well as some effects to show digital tech.

1 side to have position, name and address
2 side to have company name and show that we provide money exchange and cross-border money transfer

Target Market(s)

Remittance companies and high net worth individuals

Industry/Entity Type

Finance

Contact Information for Business Card

Name, address, email, title, services- money exchange and cross-border remittance

Requirements
Nice to have
• Digital age feel

```html
<!DOCTYPE html>
<html lang="en">
<head>
<meta charset="utf-8">
<title>Pavolex Business Card</title>
<link rel="stylesheet" href="https://fonts.googleapis.com/css2?family=Montserrat:wght@400;600;700&family=Arimo:wght@400&display=swap">
<style>
  :root {
    --bg: #e8e8e7;
    --navy: #243140;
    --navy-deep: #1f2a37;
    --navy-soft: #3a4855;
    --cyan: #5ccfe0;
    --white: #ffffff;
    --muted: #c9d3dc;
  }
  * { box-sizing: border-box; margin: 0; padding: 0; }
  html, body { width: 1200px; height: 802px; overflow: hidden; background: var(--bg); }
  .canvas { position: relative; width: 1200px; height: 802px; }

  .card {
    position: absolute;
    width: 540px;
    height: 309px;
    background: var(--navy);
    overflow: hidden;
    box-shadow: 0 10px 24px rgba(0,0,0,0.18);
    border-bottom: 5px solid var(--cyan);
  }
  .card-front { left: 45px; top: 246px; }
  .card-back { left: 615px; top: 246px; }

  .mark-backdrop {
    position: absolute;
    right: 40px; top: 50px;
    width: 240px; height: 230px;
    border-radius: 60px;
    background: radial-gradient(ellipse at center, rgba(58,72,85,0.85) 0%, rgba(58,72,85,0.35) 55%, rgba(36,49,64,0) 75%);
  }

  .corner-tab {
    position: absolute;
    right: 0; top: 0;
    width: 14px; height: 56px;
    background: var(--cyan);
  }
  .person {
    position: absolute;
    right: 28px; top: 14px;
    text-align: right;
    font-family: "Montserrat", sans-serif;
  }
  .person-name {
    color: var(--cyan);
    font-weight: 700;
    font-size: 16px;
    letter-spacing: 0.5px;
  }
  .person-title {
    color: var(--white);
    font-family: "Arimo", sans-serif;
    font-size: 12px;
    margin-top: 2px;
  }

  .brand {
    position: absolute;
    left: 36px; top: 128px;
    display: flex;
    align-items: center;
    gap: 10px;
  }
  .brand-dot {
    width: 22px; height: 22px;
    background: var(--cyan);
    border-radius: 50%;
  }
  .brand-name {
    font-family: "Montserrat", sans-serif;
    font-weight: 700;
    font-size: 30px;
    letter-spacing: 1px;
    color: var(--white);
  }

  .contact {
    position: absolute;
    left: 36px; bottom: 22px;
    font-family: "Arimo", sans-serif;
    font-size: 12.5px;
    color: var(--white);
    line-height: 1.45;
  }
  .address { margin-bottom: 6px; }
  .contact-row { display: flex; align-items: center; gap: 8px; }
  .contact-row svg { width: 12px; height: 12px; flex: none; }

  .pattern-field {
    position: absolute;
    inset: 0;
    background:
      linear-gradient(135deg, rgba(255,255,255,0.05) 0%, rgba(255,255,255,0) 45%),
      linear-gradient(180deg, var(--navy) 0%, var(--navy-deep) 100%);
  }
  .back-identity {
    position: absolute;
    right: 44px; top: 118px;
    text-align: right;
  }
  .back-brand {
    font-family: "Montserrat", sans-serif;
    font-weight: 700;
    font-size: 28px;
    letter-spacing: 1px;
    color: var(--cyan);
  }
  .services {
    margin-top: 10px;
    list-style: none;
    font-family: "Arimo", sans-serif;
    font-size: 12.5px;
    line-height: 1.6;
    color: var(--muted);
  }
</style>
</head>
<body>
<div class="canvas">

  <section class="card card-front">
    <div class="mark-backdrop" role="img" aria-label="Faint oversized brand mark decoration"></div>
    <div class="corner-tab"></div>
    <div class="person">
      <div class="person-name">DANIEL REEVES</div>
      <div class="person-title">Manager</div>
    </div>

    <div class="brand">
      <span class="brand-dot"></span>
      <span class="brand-name">PAVOLEX</span>
    </div>

    <div class="contact">
      <div class="address">48 Harbor Lane, Calder<br>Westvale, 20415</div>
      <div class="contact-row">
        <svg viewBox="0 0 24 24" fill="none" stroke="#5ccfe0" stroke-width="2.4"><path d="M5 3h4l2 5-3 2a11 11 0 0 0 6 6l2-3 5 2v4a2 2 0 0 1-2 2A17 17 0 0 1 3 5a2 2 0 0 1 2-2z"/></svg>
        <span>555-318-4072</span>
      </div>
      <div class="contact-row">
        <svg viewBox="0 0 24 24" fill="none" stroke="#5ccfe0" stroke-width="2.4"><rect x="2" y="5" width="20" height="14" rx="1"/><path d="M2 6l10 7 10-7"/></svg>
        <span>daniel@pavolex-mail.com</span>
      </div>
      <div class="contact-row">
        <svg viewBox="0 0 24 24" fill="none" stroke="#5ccfe0" stroke-width="2.2"><circle cx="12" cy="12" r="10"/><path d="M2 12h20M12 2c3 3 3 17 0 20M12 2c-3 3-3 17 0 20"/></svg>
        <span>www.pavolex-transfer.com</span>
      </div>
    </div>
  </section>

  <section class="card card-back">
    <div class="pattern-field" role="img" aria-label="Embossed repeating brand pattern across the card"></div>
    <div class="back-identity">
      <div class="back-brand">PAVOLEX</div>
      <ul class="services">
        <li>Money Exchange</li>
        <li>Cross-Border Remittance</li>
      </ul>
    </div>
  </section>

</div>
</body>
</html>
```